Football (soccer) board game app design

Hi,

We are a start up looking for a gameplay design for an app. It is a football trivia app that consists of four main screens; login/register, main navigation, gameplay, question.

OVERALL:
We want our app to be kept in a dark theme. Black or very dark gray is preferable, with a couple of nice colors to give it a stylish touch. We like flat designs, but are open for ideas within the general structure design. The logo can be used in the app, but feel free to improve it you feel you can. In the attached material we have tried to outline some of our ideas and other designs friends have helped us make.

LOGIN/REGISTER:
We want a simple login. Email, password, Chatterly login and the possibility to register a new user. Live search check whether the email is valid and free, and there is also live validation of passwords. If this could be incorporated in the design it would be nice.

MAIN NAVIGATION:
In the main navigation screen we want it to be divided into tabs. A home, my games, my categories and a ranking tab. In the top bar it should be possible to search for categories as well as there should be a button to go to settings.

The Home tab
In the home tab we want a "Quick Play" button, and a list of featured categories. A category can be unlocked or locked, which should be illustrated somehow. When a category is tapped it should divide the block into a left and right tap area, where the user can choose to "Beat to unlock" or "Buy to unlock" if locked and "Practice" or "Challenge Friend" if already unlocked.

The My Games tab
In the my games tab, the current games should be divided into three lists. First "your turn", then "opponents turn" and finally "finished games".

The My Categories tab
This tab should include a list of categories, which the user have bought, but as of design it is fairly similar to the blocks in home tab. So not much different here.

The Ranking tab
Ranking should show a set of leaderboards; Today, This Week, This Month, etc. The row in a leaderboard should have teamname and a win percentage.

GAMEPLAY:
The gameplay is inspired by an old football (soccer) board game from the 1950's, and our gameplay consists of three core elements; a football (soccer) pitch, 11 players and a scoreboard.

The football (soccer) pitch
What we need is a pitch seen from behind the goal line. The important issue here, is the perspective, as we want 11 players on the field formed as a 4-3-3 formation, being 1 goalkeeper, 4 defenders, 3 midfielder and 3 strikers. They should all be touchable without overlap. In the other end we want a goal that should be touchable as well. The goal in the nearest end do not have to be visible. Due to the perspective of the field and the fact that players and goal should be touchable, of course give you the opportunity to play around with the proportions of both players and goal. We rather want a large goal being out of proportions, than a small goal with a tiny tap area. Around the field (sidelines and beside the goal) we would like advertising banners like seen on a real stadium.

The players
As mentioned we want 11 players in a 4-3-3 formation. The players should be attached to the board with springs as seen on some of the very old board games, where you could flick the player to pass the ball. This also means that we want the players to be placed in an indentation for the ball to fall into and it would be very cool if you could illustrate the player with the ball, as being pulled back to one of the sides, just enough to see the ball at his feet. The players should be large enough for a user to tap them, hence it would also be beneficial if they are not overlapping. For a start we would like to see the players in a blue shirt and white shorts (socks are not necessary as they are placed on a spring).

Scoreboard
On the scoreboard above the field, we need information such as the names of the two teams (could be FC Brightmoor and Tall Oak Rovers), the score (2-1), minutes played (42), and which half (1st). We also want a progress bar that illustrates how many moves you have used ranging from 0-5. The scoreboard could be inspired from the ones seen around stadiums across the world, but feel free to improvise.

What We Are Looking for
We are looking for full PSD and AI files so we can use them to make minor changes like colors on shirts and shorts, colors on pitch, etc. We really want you to be innovative and inspire us, as we are not designers ourselves. In the attached files, we have tried to sketch out a design that covers our initial ideas. We are looking for a professional look, and having the players and field look like a real board game would just be awesome. A combination of the look from the realistic pitch with advertising banners around it, the idea of our spring-players and the initial thoughts of a design illustrated in our sketch, should help you along. Flat design, cartoonish or somewhere in between is up to you, we just want you to impress and make "wow"-feeling.

QUESTION:
The final screen should display a question with four possible answers. There should be a green/checkmark when correct answer, and a red/cross if incorrect.

That's all. We are looking very much forward to see your designs!
Updates

Hi all,

We have changed the terms of the contest to now have a guaranteed payment, and we are really looking forward to see your designs! Good luck.

/ Mikkel and Anders

By request we have now uploaded an AI-file with the logo for you to play around with. We are looking forward to see your designs.

/ Mikkel and Anders

Reason: Hi designers, We are really happy with the progress being made, and are looking forward to see some of the designs that are still work in progress. However the amount of designs received, has not reached our expectations yet. Therefore we are extending the deadline for seven more days, so designers, that are still working on their designs can continue their work without a stressing deadline in the horizon. Good luck to all of you. We are looking very much forward to see, what you are able to produce. Best regards, Mikkel and Anders

Reason: Hi all, We still have a lot of designers in the competition , who are battling to finish their designs, therefore we have decided to extend the deadline once more. Good luck to all of you!

Target Market(s)

Football (soccer) fans

Industry/Entity Type

Advertising

```html
<!DOCTYPE html>
<html lang="en">
<head>
<meta charset="utf-8">
<title>Football Trivia – Home</title>
<link href="https://fonts.googleapis.com/css2?family=PT+Sans&family=Roboto+Condensed:wght@700&display=swap" rel="stylesheet">
<style>
  :root {
    --bg: #1c2631;
    --tab-dark: #141b23;
    --tab-text: #c9d1d9;
    --accent: #0a9be2;
    --accent-deep: #0a7fc4;
    --panel-dark: #151d26;
    --line: #3a4651;
    --white: #ffffff;
    --lock-disc: #1b2b3a;
  }
  * { margin: 0; padding: 0; box-sizing: border-box; }
  html, body { width: 676px; height: 1200px; overflow: hidden; background: var(--bg); }
  .screen { position: relative; width: 676px; height: 1200px; background: var(--bg); overflow: hidden; }

  .tab-bar { position: absolute; left: 0; top: 0; width: 676px; height: 99px; display: flex; }
  .tab {
    flex: 1; display: flex; align-items: center; justify-content: center;
    font-family: "PT Sans", sans-serif; font-size: 23px; letter-spacing: 4px;
    color: var(--tab-text); background: var(--tab-dark); border-left: 1px solid #222c36;
  }
  .tab.active { background: var(--bg); border-left: none; position: relative; }
  .tab.active::before { content: ""; position: absolute; left: 0; top: 0; width: 100%; height: 6px; background: var(--accent); }

  .action-button {
    position: absolute; top: 116px; height: 123px; width: 318px;
    display: flex; align-items: center; justify-content: center;
    font-family: "Roboto Condensed", sans-serif; font-weight: 700; font-size: 34px; color: var(--white);
  }
  .quick-play { left: 17px; background: var(--accent); border: 1px solid #5fc1ef; }
  .challenge-friend { left: 343px; background: var(--panel-dark); border: 1px solid var(--line); color: #e6ebef; }

  .divider { position: absolute; left: 17px; top: 259px; width: 644px; height: 1px; background: #36414c; }

  .category-card { position: absolute; left: 18px; width: 643px; height: 174px; overflow: hidden; border: 1px solid #1e5a86; }
  .category-photo { position: absolute; inset: 0; }
  .category-title {
    position: absolute; left: 24px; bottom: 18px;
    font-family: "Roboto Condensed", sans-serif; font-weight: 700; font-size: 33px; color: var(--white);
    text-shadow: 0 2px 4px rgba(0,0,0,0.6);
  }
  .card-goalkeepers { top: 277px; }
  .card-goalkeepers .category-photo { background: linear-gradient(90deg, #0b0a0d 0%, #1f0c12 45%, #2c1d1a 62%, #2f5a1c 78%, #1a1413 100%); }
  .card-continental { top: 458px; }
  .card-continental .category-photo { background: linear-gradient(100deg, #5a1a1e 0%, #a83437 30%, #c9453f 55%, #8e2228 80%, #4a1216 100%); }
  .card-nordic { top: 642px; }
  .card-nordic .category-photo { background: linear-gradient(180deg, #2c3138 0%, #4a4f56 55%, #6c6f73 80%, #8c2026 100%); }

  .unlock-panel { position: absolute; left: 18px; top: 826px; width: 643px; height: 174px; background: var(--accent-deep); overflow: hidden; }
  .unlock-panel .category-photo { position: absolute; inset: 0; background: linear-gradient(90deg, #0a78ba 0%, #0e84c8 50%, #0a76b6 100%); }
  .unlock-panel .faded-title {
    position: absolute; left: 22px; top: 124px;
    font-family: "Roboto Condensed", sans-serif; font-weight: 700; font-size: 33px; color: rgba(20,50,80,0.45);
  }
  .unlock-choice {
    position: absolute; top: 14px; width: 280px; height: 148px;
    border: 1px solid rgba(160,210,240,0.55);
    display: flex; align-items: center; justify-content: center; text-align: center;
    font-family: "Roboto Condensed", sans-serif; font-weight: 700; font-size: 33px; line-height: 45px; color: var(--white);
  }
  .beat-to-unlock { left: 10px; }
  .buy-to-unlock { left: 354px; }
  .lock-disc {
    position: absolute; left: 280px; top: 48px; width: 80px; height: 80px; border-radius: 50%;
    background: var(--lock-disc); border: 3px solid #2a8fcf; display: flex; align-items: center; justify-content: center;
  }

  .card-global { top: 1011px; border: none; }
  .card-global .category-photo { background: linear-gradient(90deg, #3d3d3d 0%, #6f6f6f 35%, #8a8a8a 55%, #5c5c5c 80%, #474747 100%); }
  .card-global .category-title { color: #d8d8d8; }
  .locked-strip {
    position: absolute; right: 0; top: 0; width: 66px; height: 174px; background: var(--accent);
    display: flex; flex-direction: column; align-items: center; padding-top: 16px;
  }
  .locked-label {
    margin-top: 18px; writing-mode: vertical-rl; transform: rotate(180deg);
    font-family: "PT Sans", sans-serif; font-size: 20px; letter-spacing: 4px; color: var(--white);
  }
</style>
</head>
<body>
<div class="screen">
  <nav class="tab-bar">
    <div class="tab active">HOME</div>
    <div class="tab">MATCHES</div>
    <div class="tab">RANKINGS</div>
    <div class="tab">SETTINGS</div>
  </nav>

  <div class="action-button quick-play">Quick Play</div>
  <div class="action-button challenge-friend">Challenge Friend</div>
  <div class="divider"></div>

  <div class="category-card card-goalkeepers">
    <div class="category-photo" role="img" aria-label="Photo of a legendary goalkeeper in a green kit with arms spread"></div>
    <div class="category-title">Legendary Goalkeepers</div>
  </div>

  <div class="category-card card-continental">
    <div class="category-photo" role="img" aria-label="Photo of players in red lifting a trophy amid red confetti"></div>
    <div class="category-title">Continental Cup</div>
  </div>

  <div class="category-card card-nordic">
    <div class="category-photo" role="img" aria-label="Photo of a player in red making an overhead kick beside a defender in white"></div>
    <div class="category-title">Nordic Premier</div>
  </div>

  <div class="unlock-panel">
    <div class="category-photo" role="img" aria-label="Faded blue-tinted photo of a match"></div>
    <div class="faded-title">Italia Liga 2013/14</div>
    <div class="unlock-choice beat-to-unlock">Beat<br>To Unlock</div>
    <div class="unlock-choice buy-to-unlock">Buy<br>To Unlock</div>
    <div class="lock-disc">
      <svg width="34" height="40" viewBox="0 0 34 40" aria-hidden="true">
        <path d="M9 17 V11 a8 8 0 0 1 16 0 V17" fill="none" stroke="#fff" stroke-width="4"/>
        <rect x="3" y="17" width="28" height="21" rx="2" fill="#fff"/>
      </svg>
    </div>
  </div>

  <div class="category-card card-global">
    <div class="category-photo" role="img" aria-label="Grayscale photo of a team celebrating a title"></div>
    <div class="category-title">Global Cup 1994</div>
    <div class="locked-strip">
      <svg width="24" height="28" viewBox="0 0 24 28" aria-hidden="true">
        <path d="M6 12 V8 a6 6 0 0 1 12 0 V12" fill="none" stroke="#fff" stroke-width="3"/>
        <rect x="2" y="12" width="20" height="15" rx="1.5" fill="#fff"/>
      </svg>
      <div class="locked-label">LOCKED</div>
    </div>
  </div>
</div>
</body>
</html>
```